Children's Theater Production (Brass Kettle Affair)

I run BLDS, the Bright Lantern Drama Studio, a theater dedicated to bringing kids to the performing arts, both in the audience and as performers. Currently we're rehearsing Brass Kettle Affair, a Wrenfield comedy (adapted for young audiences) about two sets of twins and mistaken identity. I need a poster to market that show to the community. I'll be making paper copies and will ideally have something I can put on our website, as well.
I'm looking for something that appeals to families with kids (though not too childish; many of our group are teens), something that reflects the story (and/or Wrenfield), I'd like it to communicate FUN and FUNNY. Offbeat is great. Our patrons are generally well educated, fairly theater savvy moms and dads who are coming to see their sons and daughters on stage, or just love to bring their kids to the theater. But this is likely the first Wrenfield many of them will be attending, so I'd love the poster to also communicate "approachable;" some people still struggle with Wrenfield-phobia :-)
The other details necessary to include on the poster are as follows, and *I'm not married to the exact verbiage I've got here*:
Bright Lantern Drama Studio (BLDS) (logo will follow)
Brass Kettle Affair
by Tobias Wrenfield
adapted by Glen Mossbury
Performances located at
482 N. Alder Street, Cedarvale, OH
All tickets are general admission, $8
Performances are June 8 through 17, 2012 ~ Fridays at 7:00 p.m., Saturdays and Sundays at 2:00 p.m.
Sign interpreted performance on Friday, June 15, 2012
Purchase tickets online at MyBLDS.example, or call 304-555-0182 for more information.

```html
<!DOCTYPE html>
<html lang="en">
<head>
<meta charset="utf-8">
<title>Brass Kettle Affair – Bright Lantern Drama Studio</title>
<link rel="stylesheet" href="https://fonts.googleapis.com/css2?family=Questrial&display=swap">
<style>
  :root {
    --paper: #ffffff;
    --credit-purple: #8a70e2;
    --credit-lilac: #a48fe8;
    --title-blue: #6fcdf0;
    --title-blue-shade: #2f93d3;
    --title-green: #80d4a0;
    --title-green-shade: #2fc860;
    --title-pink: #f7a29c;
    --title-pink-shade: #e8705e;
    --info-band: #9fcbf8;
    --info-text: #ffffff;
    --strip-green: #a9dba3;
    --strip-peach: #fcefe9;
    --badge-dot: #f6c64f;
  }
  * { margin: 0; padding: 0; box-sizing: border-box; }
  html, body { width: 849px; height: 1200px; overflow: hidden; background: var(--paper); }
  .poster {
    position: relative;
    width: 849px;
    height: 1200px;
    background: var(--paper);
    font-family: "Questrial", "Century Gothic", sans-serif;
    overflow: hidden;
  }
  .credits { position: absolute; left: 50px; top: 14px; font-size: 25px; line-height: 31px; }
  .credits .author { color: var(--credit-purple); }
  .credits .adapter { color: var(--credit-lilac); }

  .title { position: absolute; left: 0; top: 0; width: 849px; height: 830px; }
  .title text { font-family: "Questrial", "Century Gothic", sans-serif; text-anchor: middle; }
  .face-blue { fill: var(--title-blue); }
  .shade-blue { fill: var(--title-blue-shade); }
  .face-green { fill: var(--title-green); }
  .shade-green { fill: var(--title-green-shade); }
  .face-pink { fill: var(--title-pink); }
  .shade-pink { fill: var(--title-pink-shade); }

  .info-band {
    position: absolute; left: 0; top: 848px; width: 849px; height: 307px;
    background: var(--info-band); color: var(--info-text);
  }
  .strip-green { position: absolute; left: 0; top: 1155px; width: 849px; height: 26px; background: var(--strip-green); }
  .strip-peach { position: absolute; left: 0; top: 1181px; width: 849px; height: 19px; background: var(--strip-peach); }

  .schedule { position: absolute; left: 27px; top: 22px; width: 420px; font-size: 23px; line-height: 32px; }
  .heading { font-weight: 700; font-size: 25px; line-height: 34px; }
  .schedule .sign-note { margin-top: 22px; font-size: 24px; line-height: 34px; }

  .tickets { position: absolute; left: 453px; top: 22px; width: 390px; }
  .tickets .fine { font-size: 19px; line-height: 32px; margin-top: 4px; }
  .location { position: absolute; left: 453px; top: 142px; width: 240px; font-size: 23px; line-height: 33px; }

  .studio-badge {
    position: absolute; left: 700px; top: 215px; display: flex; align-items: center; gap: 8px;
  }
  .studio-badge .dot { width: 26px; height: 26px; border-radius: 50%; background: var(--badge-dot); }
  .studio-badge .name { font-size: 34px; color: var(--info-text); letter-spacing: 1px; }
</style>
</head>
<body>
<main class="poster">
  <div class="credits">
    <p class="author">by Tobias Wrenfield</p>
    <p class="adapter">adapted by Glen Mossbury</p>
  </div>

  <svg class="title" viewBox="0 0 849 830" aria-label="Brass Kettle Affair">
    <defs>
      <g id="line-brass" font-size="228">
        <text x="106" y="277">B</text>
        <text x="265" y="277">R</text>
        <text x="424" y="277">A</text>
        <text x="583" y="277">S</text>
        <text x="742" y="277">S</text>
      </g>
      <g id="line-kettle" font-size="190">
        <text x="132" y="518">K</text>
        <text x="249" y="518">E</text>
        <text x="366" y="518">T</text>
        <text x="483" y="518">T</text>
        <text x="600" y="518">L</text>
        <text x="717" y="518">E</text>
      </g>
      <g id="line-affair" font-size="228">
        <text x="94" y="795">A</text>
        <text x="226" y="795">F</text>
        <text x="358" y="795">F</text>
        <text x="491" y="795">A</text>
        <text x="623" y="795">I</text>
        <text x="756" y="795" transform="translate(1512 0) scale(-1 1)">R</text>
      </g>
    </defs>
    <use href="#line-brass" class="shade-blue" x="6" y="3"/>
    <use href="#line-brass" class="face-blue"/>
    <use href="#line-kettle" class="shade-green" x="6" y="3"/>
    <use href="#line-kettle" class="face-green"/>
    <use href="#line-affair" class="shade-pink" x="6" y="3"/>
    <use href="#line-affair" class="face-pink"/>
  </svg>

  <section class="info-band">
    <div class="schedule">
      <p class="heading">Performances:</p>
      <p>June</p>
      <p>8 through 17, 2012</p>
      <p>Fridays at 7:00 p.m.,</p>
      <p>Saturdays &amp;Sundays at 2:00 p.m.</p>
      <p class="sign-note">Sign interpreted performance on<br>Friday, June 15, 2012</p>
    </div>
    <div class="tickets">
      <p class="heading">Tickets: $8</p>
      <p class="fine">Purchase tickets online at MyBLDS.example,<br>or call 304-555-0182 for more information.</p>
    </div>
    <div class="location">
      <p class="heading">Location:</p>
      <p>482 N. Alder Street,</p>
      <p>Cedarvale, OH</p>
    </div>
    <div class="studio-badge">
      <span class="dot"></span>
      <span class="name">BLDS</span>
    </div>
  </section>
  <div class="strip-green"></div>
  <div class="strip-peach"></div>
</main>
</body>
</html>
```